KVR Associates needs a web site

We need a web site for www.kvrassociates-example.com. KVR is a mergers and acquisition consulting company that focuses our buyer and seller services on logistics companies. We help put companies together, and help with legal and financial due diligence. We want the web site to express our service and show the logistics components. We want personalized images versus pictures of trucks and airplanes.

Our new logo uses Burgandy and grey colors. Image attached. We are not in to bold, big letters...classy, artistic, low key preferred. Confidentiality, experience, professional are what we want to express on the site.

All we expect for the first part of this project is a home page, and one subpage.  We are budgeting other funds for the technical aspects of the web site

Reason: All that I'm seeing so far is trucks, forklifts and planes. We are a legal mergers and acquisitions firm that focus on logistics. I like some of the images to say logistics, but really want it say legal, financial, and putting companies together. Will pay extra for the sub page if someone can impress us with a home page.

Reason: Swamped with another project at the moment...will work on this over the weekend and provide designer feedback and select final design by Tuesday

```html
<!DOCTYPE html>
<html lang="en">
<head>
<meta charset="utf-8">
<title>KVR Associates</title>
<link href="https://fonts.googleapis.com/css2?family=Open+Sans:wght@400;600;700&display=swap" rel="stylesheet">
<style>
:root{
  --burgundy:#8e1538;
  --burgundy-dark:#6d0f2a;
  --grey-light:#f1f1f1;
  --grey-hero:#e6e6e6;
  --grey-text:#6b6b6b;
  --grey-dark:#3a3a3a;
  --footer:#2a2a2a;
  --white:#ffffff;
}
*{box-sizing:border-box;margin:0;padding:0}
html,body{width:831px;height:1200px;overflow:hidden}
body{font-family:"Open Sans",Arial,sans-serif;color:var(--grey-dark);background:var(--white);position:relative}

.site-header{position:absolute;top:0;left:0;width:831px;height:125px;background:linear-gradient(#fafafa,#ececec)}
.brand{position:absolute;left:34px;top:38px;display:flex;align-items:center;gap:10px}
.brand-mark{width:14px;height:14px;background:var(--burgundy)}
.brand-name{font-size:26px;font-weight:600;color:var(--burgundy);letter-spacing:1px}
.brand-sub{font-size:10px;font-weight:600;color:var(--grey-text);line-height:1.25;letter-spacing:.5px;text-transform:uppercase;border-left:1px solid #bbb;padding-left:10px}
.main-nav{position:absolute;left:332px;top:28px;width:499px;height:97px;background:linear-gradient(#a01a42,var(--burgundy-dark));display:flex}
.nav-item{flex:1;display:flex;flex-direction:column;align-items:center;justify-content:center;gap:10px;color:var(--white);font-size:11px;font-weight:600;text-transform:uppercase;border-left:1px solid rgba(255,255,255,.15)}
.nav-item.active{background:rgba(0,0,0,.18)}
.nav-item svg{width:26px;height:26px;fill:var(--white)}

.hero{position:absolute;top:125px;left:0;width:831px;height:290px;background:var(--grey-hero)}
.hero-photo{position:absolute;right:0;top:0;width:443px;height:290px;background:linear-gradient(110deg,#d8dde2,#b8c0c8 55%,#e9ecef)}
.hero-copy{position:absolute;left:34px;top:68px;width:330px}
.hero-title{font-size:20px;font-weight:600;color:var(--grey-dark);letter-spacing:1px;text-transform:uppercase;margin-bottom:12px}
.hero-text{font-size:10px;line-height:1.5;color:var(--grey-text)}
.hero-actions{position:absolute;left:34px;top:228px;display:flex;gap:10px}
.btn{display:inline-flex;align-items:center;gap:6px;background:var(--burgundy);color:var(--white);font-size:10px;padding:6px 14px;border-radius:2px}
.btn.dark{background:var(--grey-dark)}

.section-title{position:absolute;left:34px;font-size:16px;letter-spacing:1px;text-transform:uppercase;color:var(--grey-dark)}
.section-title em{font-style:normal;color:var(--burgundy)}
.section-rule{position:absolute;left:34px;width:763px;height:1px;background:#d6d6d6}
.welcome-title{top:460px}
.welcome-rule{top:496px}

.features{position:absolute;left:34px;top:532px;width:763px;display:flex;justify-content:space-between}
.feature{width:170px;text-align:center}
.feature-image{height:118px;border:3px solid #ddd}
.feature-image.services{background:linear-gradient(135deg,#7fa8cc,#2f5f8d)}
.feature-image.news{background:linear-gradient(135deg,#d7d7d7,#8a8a8a)}
.feature-image.about{background:linear-gradient(135deg,#c9ced3,#6f7a85)}
.feature-image.contact{background:linear-gradient(135deg,#f2f2f2,#a7a7a7)}
.feature-title{margin-top:12px;font-size:14px;color:var(--burgundy);text-transform:uppercase}
.feature-text{margin-top:4px;font-size:10px;line-height:1.35;color:var(--grey-text)}
.feature .btn{margin-top:8px;padding:3px 12px;font-size:9px}

.testimonials-title{top:790px}
.testimonials-rule{top:826px}
.slider-dots{position:absolute;right:34px;top:800px;display:flex;gap:5px}
.slider-dots span{width:8px;height:8px;border-radius:50%;background:#ccc}
.slider-dots span.on{background:var(--burgundy)}
.quotes{position:absolute;left:34px;top:845px;width:763px;display:flex;justify-content:space-between}
.quote{width:360px;position:relative;padding-left:24px}
.quote-mark{position:absolute;left:0;top:-6px;font-size:34px;color:#bbb;line-height:1}
.quote-text{font-size:10px;line-height:1.5;color:var(--grey-text)}
.quote-author{margin-top:6px;font-size:9px;color:var(--burgundy)}
.testimonials-action{position:absolute;top:992px;left:0;width:831px;text-align:center}
.testimonials-action .btn{background:var(--grey-dark);font-size:9px;text-transform:uppercase;padding:6px 12px}

.site-footer{position:absolute;top:1052px;left:0;width:831px;height:148px;background:var(--footer)}
.newsletter{position:absolute;left:0;top:56px;width:831px;display:flex;justify-content:center;align-items:center;gap:14px}
.newsletter-label{color:var(--white);font-size:14px;letter-spacing:1px;text-transform:uppercase}
.newsletter-input{width:220px;height:26px;background:var(--white);font-size:10px;color:#999;padding:6px 10px}
.newsletter .btn{font-size:10px;text-transform:uppercase;padding:6px 12px}
.footer-bar{position:absolute;left:0;bottom:0;width:831px;height:37px;background:var(--burgundy);display:flex;justify-content:space-between;align-items:center;padding:0 92px}
.copyright{color:var(--white);font-size:10px}
.social{display:flex;gap:6px}
.social span{width:18px;height:18px;border-radius:50%;background:var(--white)}
</style>
</head>
<body>

<header class="site-header">
  <div class="brand">
    <span class="brand-mark"></span>
    <span class="brand-name">KVR</span>
    <span class="brand-sub">KVR<br>Associates</span>
  </div>
  <nav class="main-nav">
    <div class="nav-item active">
      <svg viewBox="0 0 24 24"><path d="M12 3 2 12h3v8h5v-5h4v5h5v-8h3z"/></svg>Home
    </div>
    <div class="nav-item">
      <svg viewBox="0 0 24 24"><path d="M4 8h4a2 2 0 1 1 4 0h4v4a2 2 0 1 1 0 4v4H4z"/></svg>Services ▾
    </div>
    <div class="nav-item">
      <svg viewBox="0 0 24 24"><path d="M3 4h15v15a1 1 0 0 0 2 0V8h2v11a3 3 0 0 1-3 3H5a2 2 0 0 1-2-2zm3 3v4h5V7zm7 0v1h3V7zm0 3v1h3v-1zM6 13v1h10v-1zm0 3v1h10v-1z"/></svg>Newsletters
    </div>
    <div class="nav-item">
      <svg viewBox="0 0 24 24"><circle cx="8" cy="8" r="3.5"/><circle cx="16" cy="8" r="3.5"/><path d="M1 20c0-4 3-7 7-7s7 3 7 7zm14-6.8c4 0 8 2 8 6.8h-6c0-2.8-.8-5-2-6.8z"/></svg>About Us
    </div>
    <div class="nav-item">
      <svg viewBox="0 0 24 24"><path d="M2 5h20v14H2zm2 2v.5l8 5.5 8-5.5V7z"/></svg>Contact Us
    </div>
  </nav>
</header>

<section class="hero">
  <div class="hero-photo" role="img" aria-label="Two business advisors shaking hands in a bright office"></div>
  <div class="hero-copy">
    <h1 class="hero-title">KVR Associates</h1>
    <p class="hero-text">KVR Associates, LLC guides owners of logistics businesses through growth plans and well-timed exits. Our work covers buyer and seller advisory for mergers and acquisitions, legal and financial due diligence, and discreet support in bringing companies together. Our partners bring long careers and trusted relationships across the logistics sector.</p>
  </div>
  <div class="hero-actions">
    <span class="btn">Read more ›</span>
    <span class="btn dark">Contact us ›</span>
  </div>
</section>

<h2 class="section-title welcome-title">Welcome to <em>KVR Associates</em></h2>
<div class="section-rule welcome-rule"></div>

<div class="features">
  <div class="feature">
    <div class="feature-image services" role="img" aria-label="Hands fitting puzzle pieces together"></div>
    <h3 class="feature-title">Our Services</h3>
    <p class="feature-text">Lorem ipsum dolor sit amet, consectetur adipiscing elit. Morbi nisl dignis etiam aliquet elit.</p>
    <span class="btn">more details ›</span>
  </div>
  <div class="feature">
    <div class="feature-image news" role="img" aria-label="Stack of folded newspapers"></div>
    <h3 class="feature-title">Newsletters</h3>
    <p class="feature-text">Lorem ipsum dolor sit amet, consectetur adipiscing elit. Morbi nisl dignis etiam aliquet elit.</p>
    <span class="btn">more details ›</span>
  </div>
  <div class="feature">
    <div class="feature-image about" role="img" aria-label="Business meeting around a table"></div>
    <h3 class="feature-title">About Us</h3>
    <p class="feature-text">Lorem ipsum dolor sit amet, consectetur adipiscing elit. Morbi nisl dignis etiam aliquet elit.</p>
    <span class="btn">more details ›</span>
  </div>
  <div class="feature">
    <div class="feature-image contact" role="img" aria-label="Mailbox with letters"></div>
    <h3 class="feature-title">Contact Us</h3>
    <p class="feature-text">Lorem ipsum dolor sit amet, consectetur adipiscing elit. Morbi nisl dignis etiam aliquet elit.</p>
    <span class="btn">more details ›</span>
  </div>
</div>

<h2 class="section-title testimonials-title">Client <em>Testimonials</em></h2>
<div class="slider-dots"><span class="on"></span><span></span></div>
<div class="section-rule testimonials-rule"></div>

<div class="quotes">
  <blockquote class="quote">
    <span class="quote-mark">“</span>
    <p class="quote-text">Lorem ipsum dolor sit amet, consectetur adipiscing elit. Phasellus tincidunt tellus leo, sodales vestibulum urna. Maecenas hendrerit tincidunt, ut pretium tortor non tincidunt urna. Tincidunt tellus leo, sodales vestibulum urna.</p>
    <p class="quote-author">- Alex Reed, Manager</p>
  </blockquote>
  <blockquote class="quote">
    <span class="quote-mark">“</span>
    <p class="quote-text">Lorem ipsum dolor sit amet, consectetur adipiscing elit. Phasellus tincidunt tellus leo, sodales vestibulum urna. Maecenas hendrerit tincidunt, ut pretium tortor non tincidunt urna. Tincidunt tellus leo, sodales vestibulum urna.</p>
    <p class="quote-author">- Alex Reed, Manager</p>
  </blockquote>
</div>

<div class="testimonials-action"><span class="btn">View all testimonials</span></div>

<footer class="site-footer">
  <div class="newsletter">
    <span class="newsletter-label">Subscribe to our newsletter:</span>
    <span class="newsletter-input">Email Address</span>
    <span class="btn">Subscribe</span>
  </div>
  <div class="footer-bar">
    <span class="copyright">KVR Associates All Rights Reserved © 2014</span>
    <div class="social"><span></span><span></span><span></span><span></span></div>
  </div>
</footer>

</body>
</html>
```